Metal Fabrication Business Cards

We need a business card for our business of Metal Fabrication/Welding. Our company is called "Hadley's Metal Fabrication"

We are a metal fabrication business which takes on "high class" clients- dealing with some of the biggest builders in Australia. Our work is neat, and the type of work we do is 2nd to none for quality. We want to show that on our cards. However, we would love to show a side that is down to earth and a bit more modern and contemporary - we are all young in business so would love to show that side - rather than a boring "very straight looking" card. We always have a clean workshop and take pride in our presentation. We want to come across like we are very rich, but would love to go for a surf as well! A card that basically says we have high class and will charge you a high rate - but the quality will be outstanding.

Front of card: - Simply but sharp!
-Thinking maybe white card - with nice black writing.
-On the right hand side of card a person welding - or holding a welder.
- My business name - Hadley's Metal Fabrication
-Also maybe my name - which is 'Corey" (if it doesn't work, we can put this on the back of card.)
- if needed to look better - we can put keywords on front of card like "metal fabrication, sheet metal, welding etc" but I dont want it to be crowded.

Back of card: - Also make smart but sharp!
Put details such as:
04387 21 914
hadley.fabrication@tinmailbox.com.au
7/32 Keel Street
South Lismore NSW 2480
www.korvinfabrication.com.au
ABN 72 615 803 914

thats just an idea - its now up to you. I don't mind what you come up with - as long as it stands out from the rest and looks sharp, professional but contemporary.

Business

Put details such as:
04387 21 914
7/32 Keel Street
South Lismore NSW 2480
ABN 72 615 803 914

Hadley's Metal Fabrication

```html
<!DOCTYPE html>
<html lang="en">
<head>
<meta charset="utf-8">
<title>Hadley's Metal Fabrication — Business Cards</title>
<link rel="stylesheet" href="https://fonts.googleapis.com/css2?family=Cormorant+SC:wght@600;700&family=Tinos:wght@400&display=swap">
<style>
  :root {
    --page-bg: #e9e6e1;
    --card-white: #f7f7f5;
    --ink: #151515;
    --illustration-tone: #d9d9d6;
    --illustration-faint: #ecebe8;
    --card-shadow: rgba(0, 0, 0, 0.18);
  }

  * { box-sizing: border-box; margin: 0; padding: 0; }

  html, body {
    width: 1200px;
    height: 900px;
    overflow: hidden;
    background: var(--page-bg);
  }

  .canvas {
    width: 1200px;
    height: 900px;
    display: flex;
    align-items: center;
    justify-content: center;
    gap: 48px;
  }

  .business-card {
    position: relative;
    width: 540px;
    height: 330px;
    background: var(--card-white);
    box-shadow: 0 6px 18px var(--card-shadow);
    overflow: hidden;
    color: var(--ink);
  }

  /* Front */
  .card-front .company-name {
    position: absolute;
    z-index: 2;
    top: 40px;
    left: 34px;
    font-family: "Cormorant SC", "Times New Roman", serif;
    font-weight: 700;
    font-size: 40px;
    line-height: 1.1;
    letter-spacing: 2px;
    white-space: nowrap;
  }

  .company-name span { display: block; }
  .company-name .line-metal { margin-left: 30px; }
  .company-name .line-fabrication { margin-left: 60px; }

  .card-front .welder-illustration {
    position: absolute;
    z-index: 1;
    right: 20px;
    bottom: 40px;
    width: 160px;
    height: 170px;
    border-radius: 46% 40% 30% 36%;
    background: radial-gradient(circle at 55% 45%, var(--illustration-tone), var(--card-white) 75%);
  }

  /* Back */
  .card-back .contact-list {
    position: absolute;
    top: 34px;
    left: 38px;
    list-style: none;
    font-family: "Tinos", "Times New Roman", serif;
    font-size: 17px;
    line-height: 1.5;
  }

  .contact-list li::before {
    content: "";
    display: inline-block;
    width: 6px;
    height: 6px;
    margin-right: 10px;
    border-radius: 50%;
    background: var(--ink);
    vertical-align: middle;
  }

  .card-back .welder-watermark {
    position: absolute;
    right: 30px;
    bottom: 26px;
    width: 160px;
    height: 150px;
    border-radius: 46% 40% 30% 36%;
    background: radial-gradient(circle at 55% 45%, var(--illustration-faint), var(--card-white) 75%);
  }
</style>
</head>
<body>
  <main class="canvas">
    <section class="business-card card-front">
      <h1 class="company-name">
        <span class="line-hadleys">Hadley's</span>
        <span class="line-metal">Metal</span>
        <span class="line-fabrication">Fabrication</span>
      </h1>
      <div class="welder-illustration" role="img" aria-label="Line drawing of a welder in a helmet holding a welding torch with sparks"></div>
    </section>

    <section class="business-card card-back">
      <ul class="contact-list">
        <li>04387 21 914</li>
        <li>hadley.fabrication@tinmailbox.com.au</li>
        <li>7/32 Keel Street</li>
        <li>South Lismore, NSW 2480</li>
        <li>www.korvinfabrication.com.au</li>
        <li>ABN 72 615 803 914</li>
      </ul>
      <div class="welder-watermark" role="img" aria-label="Faint line drawing of a welder at work"></div>
    </section>
  </main>
</body>
</html>
```